QBT Web Design Project

I would like a simple and elegant design for my international business consulting practice web site. I already have new QBT Logo and will have brochure-colors are blue, green and black

Practice areas:
I offer consulting services specializing in developing Internet-based anti-counterfeiting and anti-fraud programs, test purchases and investigations.

I offer Cyber Security, Data Protection and Compliance services

I also offer International Due Diligence Investigations and Country and Travel Risk Assessments

General Background Investigations

Physical Security Services

About me section listing my Bio

I have a set of key associates that I work with around the world and will want to list their CVs or Bios under "QBT

Associates"Banner with nice photo but not too cluttered

Ability to Upload documents and articles

Contact us section
Updates

I have uploaded my new logo-please advise if you didn't get it or it is not in the correct file format.

Thank you

Gordon

Hello Everyone,

Thank you for your submissions and ideas. I'm not sure about design only vs code. I understand that some of you do not do code-if not then please just provide design.

More about my business: see below link on Searchwell docs to my brochure-this should help but don't use that phone number-see below.

https://files.example-docs.net/viewer?id=XK93PLQ7ZTR2MWN8&hl=en_US

 

Here are some details.

Contacts:

Gordon T. Vostrell, CPP

President

Vostrell and Partners, LLC

P.O. Box 47192

Gaithersburg, MD 20899

USA

web address:www.Vostrellandpartners.example (currently not working)

email:gord @vostrelland partners.example

Tel: 202-555-0147

I hope this is helpful. Gord

Reason: Sorry but during holiday period, have not had as much time to devote to this project. Thanks for your submissions.

Per my previous guidance, please keep designs simple and elegant and free from traditional security images with locks and chains-I prefer one or at most, two photos. Two colors- blue and green in addition to black for print. I want to present professional, corporate and international image. Thank you for your ideas nad submissions.

Gord

Target Market(s)

Law firms, large multi-national corporations, Security Industry

Industry/Entity Type

Business

Requirements
Must have
• Must have sections: (will provide text)

About QBT (will provide text)

Practice areas

Associates (will provide text)

Contact us

(it must also have ability to upload files and articles)
Should not have
• Old style fonts and symbols such as security badges, scales of justice, etc. I want a sleek and modern design.

```html
<!DOCTYPE html>
<html lang="en">
<head>
<meta charset="utf-8">
<title>QBT — Vostrell &amp; Partners, LLC</title>
<link rel="stylesheet" href="https://fonts.googleapis.com/css2?family=PT+Sans:wght@400;700&family=Didact+Gothic&display=swap">
<style>
:root{
  --page-bg:#f1f1f1;
  --sheet:#fbfbfb;
  --blue-dark:#0d5595;
  --blue:#1a6fb4;
  --blue-light:#2e8fd6;
  --green:#5fa314;
  --green-head:#5a9e1a;
  --ink:#333;
  --field:#fff;
  --field-line:#c9c9c9;
}
*{box-sizing:border-box;margin:0;padding:0}
html,body{width:1200px;height:1186px;overflow:hidden;background:var(--page-bg)}
body{position:relative;font-family:"Didact Gothic",sans-serif;color:var(--ink)}
.sheet{position:absolute;left:158px;top:11px;width:879px;height:1145px;background:linear-gradient(#fff,var(--sheet));box-shadow:0 0 10px rgba(0,0,0,.12)}
.abs{position:absolute}
.brand{left:192px;top:42px;display:flex;align-items:center;gap:8px}
.brand-mark{font-family:"PT Sans",sans-serif;font-size:25px;color:var(--blue);padding-right:7px;border-right:1px solid #7a9cc0;line-height:28px}
.brand-name{font-family:"PT Sans",sans-serif;font-size:22px;color:#222}
.brand-tag{left:193px;top:73px;font-family:"PT Sans",sans-serif;font-size:12.5px;letter-spacing:2px;color:var(--blue)}
.search{left:788px;top:55px;width:187px;height:22px;border:1px solid #aaa;border-radius:11px;background:linear-gradient(#fff,#eee);font-family:"PT Sans",sans-serif;font-size:13px;padding-left:28px;line-height:20px;color:#222}
.search svg{position:absolute;left:6px;top:3px}
.search-ok{left:988px;top:55px;width:27px;height:22px;border:1px solid #999;border-radius:3px;background:linear-gradient(#fff,#ddd);font:12px "PT Sans",sans-serif;text-align:center;line-height:20px}
.band{left:142px;width:908px;background:linear-gradient(var(--blue-dark),#1664a6 50%,var(--blue-dark))}
.band::before,.band::after{content:"";position:absolute;top:-10px;border-bottom:10px solid #0a3f6e}
.band::before{left:0;border-left:16px solid transparent}
.band::after{right:0;border-right:16px solid transparent}
.nav{top:125px;height:54px;display:flex;justify-content:center;gap:20px;align-items:center}
.nav a{color:#fff;text-decoration:none;font-family:"PT Sans",sans-serif;font-size:17px}
.hero{left:171px;top:179px;width:852px;height:271px;border-radius:0 0 8px 8px;background:linear-gradient(var(--blue),var(--blue-light))}
.service{left:188px;width:340px;height:40px;border-radius:4px;background:linear-gradient(#1a6fb0,#1560a0);color:#fff;font-family:"PT Sans",sans-serif;font-size:13px;text-align:center;line-height:40px;box-shadow:0 1px 2px rgba(0,0,0,.25)}
.service.active{background:linear-gradient(#77bb1e,var(--green));font-size:12px}
.slide{left:551px;top:195px;width:460px;height:221px;border:6px solid #fff;border-radius:5px;background:linear-gradient(135deg,#1d6fd0,#4c9af0 50%,#7e8fd4)}
.dots{left:921px;top:389px;display:flex;gap:8px}
.dots i{width:11px;height:11px;border-radius:50%;background:#fff}
.dots i:first-child{background:var(--green)}
h2{font-family:"PT Sans",sans-serif;font-weight:400;font-size:17px;color:var(--green-head)}
.copy{font-size:13px;line-height:17px;color:var(--ink);text-indent:14px}
h3{font-family:"PT Sans",sans-serif;font-weight:400;font-size:17px;line-height:21px;color:var(--blue)}
.field{left:801px;width:132px;height:22px;border:1px solid var(--field-line);border-radius:5px;background:var(--field);font-size:8px;padding-left:7px;line-height:20px;color:#666}
.message{left:801px;top:591px;width:190px;height:114px;border:1px solid var(--field-line);border-radius:5px;background:var(--field)}
.btn{top:717px;height:22px;border:1px solid #aaa;border-radius:5px;background:linear-gradient(#fff,#e4e4e4);font:12px "PT Sans",sans-serif;text-align:center;line-height:20px;color:#444}
.partner{top:1022px;font-family:"PT Sans",sans-serif;font-weight:700;font-size:22px;color:var(--blue);display:flex;align-items:center;gap:6px;white-space:nowrap}
.partner b{display:inline-block;width:12px;height:12px;border-radius:50%;background:var(--blue)}
.footer{top:1102px;height:54px;color:#fff;font-family:"PT Sans",sans-serif;font-size:13px}
.footer span{position:absolute;top:19px}
.footer .social{right:40px;top:14px;font-size:21px;font-weight:700}
</style>
</head>
<body>
<div class="sheet"></div>

<header>
  <div class="abs brand"><span class="brand-mark">QBT</span><span class="brand-name">Vostrell &amp; Partners, LLC</span></div>
  <div class="abs brand-tag">Intellectual Property and Cyber Security</div>
  <div class="abs search"><svg width="18" height="14" viewBox="0 0 18 14"><circle cx="6" cy="6" r="4" fill="none" stroke="#555" stroke-width="1.6"/><path d="M9 9l3 3M13 5l2 2 2-2" stroke="#555" stroke-width="1.6" fill="none"/></svg>Search</div>
  <div class="abs search-ok">OK</div>
</header>

<nav class="abs band nav"><a href="#">Home</a><a href="#">About us</a><a href="#">Practice Area</a><a href="#">Careers</a><a href="#">Media</a><a href="#">Contact us</a></nav>

<section class="abs hero"></section>
<div class="abs service active" style="top:197px">Cyber Security, Data Protection and Compliance services</div>
<div class="abs service" style="top:257px">International Due Diligence Investigations</div>
<div class="abs service" style="top:320px">Country and Travel Risk Assessments</div>
<div class="abs service" style="top:376px">Physical Security Services</div>
<div class="abs slide" role="img" aria-label="Photo of a gloved hand holding a glass test tube in front of blue binary code"></div>
<div class="abs dots"><i></i><i></i><i></i><i></i></div>

<section>
  <h2 class="abs" style="left:209px;top:470px">ABOUT US</h2>
  <p class="abs copy" style="left:203px;top:498px;width:265px">Lorem ipsum dolor sit amet, consectetuer adipiscing elit, sed diam nonummy nibh euismod tincidunt ut laoreet dolore magna aliquam erat volutpat. Ut wisi enim ad minim veniam, quis nostrud exerci tation ullamcorper suscipit lobortis nisl ut aliquip ex ea commodo consequat. Duis autem vel eum iriure dolor in hendrerit in vulputate velit esse molestie consequat, vel illum dolore eu feugiat nulla facilisis at vero eros et accumsan et iusto odio dignissim qui blandit praesent luptatum zzril delenit augue duis dolore te feugait.</p>
  <h2 class="abs" style="left:497px;top:468px">WHAT WE DO</h2>
  <p class="abs copy" style="left:491px;top:496px;width:262px">Epsum factorial non deposit quid pro quo hic escorol. Olypian quarrels et gorilla congolium sic ad nauseum. Souvlaki ignitus carborundum e pluribus unum. Defacto lingo est igpay atinlay. Marquee selectus non provisio incongruous feline nolo contendre. Gratuitous octopus niacin, sodium glutimate. Quote meon an estimate et non interruptus stadium. Sic tempus fugit esperanto hiccup estrogen. Glorious baklava ex librus hup hey ad infinitum. Non sequitur condominium facile et geranium incognito.</p>
</section>

<section>
  <h2 class="abs" style="left:801px;top:466px">CONTACT US</h2>
  <div class="abs field" style="top:501px">FULL NAME</div>
  <div class="abs field" style="top:530px">EMAIL</div>
  <div class="abs field" style="top:560px">ADDRESS</div>
  <div class="abs message"></div>
  <div class="abs btn" style="left:847px;width:94px">Attach a File</div>
  <div class="abs btn" style="left:950px;width:59px">Send</div>
</section>

<section>
  <h2 class="abs" style="left:208px;top:755px">PRACTICE AREA</h2>
  <h3 class="abs" style="left:211px;top:797px">Cyber Security</h3>
  <h3 class="abs" style="left:407px;top:789px;width:150px">International Investigations</h3>
  <h3 class="abs" style="left:603px;top:800px">Travel risk Assessments</h3>
  <h3 class="abs" style="left:800px;top:802px">Physical Security</h3>
  <p class="abs copy" style="left:207px;top:838px;width:185px">Li Europan lingues es membres del sam familie. Lor separat existentie es un myth. Por scientie, musica, sport etc, li tot Europa usa li sam vocabularium. Li lingues differe solmen in li grammatica.</p>
  <p class="abs copy" style="left:405px;top:837px;width:185px">Li Europan lingues es membres del sam familie. Lor separat existentie es un myth. Por scientie, musica, sport etc, li tot Europa usa li sam vocabularium. Li lingues differe solmen in li grammatica.</p>
  <p class="abs copy" style="left:602px;top:834px;width:185px">Li Europan lingues es membres del sam familie. Lor separat existentie es un myth. Por scientie, musica, sport etc, li tot Europa usa li sam vocabularium. Li lingues differe solmen in li grammatica.</p>
  <p class="abs copy" style="left:801px;top:836px;width:185px">Li Europan lingues es membres del sam familie. Lor separat existentie es un myth. Por scientie, musica, sport etc, li tot Europa usa li sam vocabularium. Li lingues differe solmen in li grammatica.</p>
</section>

<section>
  <h2 class="abs" style="left:205px;top:1010px;line-height:21px">ASSOCIATIONS &nbsp;WE<br>&nbsp;WORK WITH</h2>
  <div class="abs partner" style="left:378px"><b></b>Nimbara</div>
  <div class="abs partner" style="left:502px">Searchwell</div>
  <div class="abs partner" style="left:658px"><b></b>Hostivane</div>
  <div class="abs partner" style="left:870px">Quorvane</div>
</section>

<footer class="abs band footer">
  <span style="left:47px">© 2011 QBT</span>
  <span style="left:145px">Privacy Policy | Copyright | Site Map | Contact Us</span>
  <span class="social">Friendhub Chirpline</span>
</footer>
</body>
</html>
```